dkfarrowplace website

I need a new homepage design for my current website at www.DKFarrowPlace.example. I want someone to look at my current website and develop a more appealing homepage... right now the colors don't blend very well and it needs a facelift

Reason: This has been extended to September 10th

```html
<!DOCTYPE html>
<html lang="en">
<head>
<meta charset="utf-8">
<title>DK Farrow — Home</title>
<link href="https://fonts.googleapis.com/css2?family=Nunito+Sans:wght@300;400;600&display=swap" rel="stylesheet">
<style>
:root{
  --hero-bg:#e7d8e5;
  --hero-bloom:#dcbfd8;
  --mauve:#b482b4;
  --pink:#d98cc1;
  --heading:#c28fc4;
  --body-text:#8c8c8c;
  --footer-bg:#d7bad7;
  --footer-text:#ffffff;
  --white:#ffffff;
  --logo-grey:#555555;
  --dark:#333333;
}
*{margin:0;padding:0;box-sizing:border-box}
html,body{width:1200px;height:2246px;overflow:hidden;background:var(--white)}
body{position:relative;font-family:"Nunito Sans",Arial,sans-serif;color:var(--body-text)}
.abs{position:absolute}

/* Hero */
.hero{position:absolute;left:0;top:0;width:1200px;height:479px;
  background:radial-gradient(ellipse at 85% 45%,var(--hero-bloom) 0%,rgba(220,191,216,0) 55%),
             radial-gradient(ellipse at 20% 95%,var(--hero-bloom) 0%,rgba(220,191,216,0) 40%),
             var(--hero-bg)}
.brand{font-size:30px;font-weight:400;color:var(--white);letter-spacing:1px}
.nav{display:flex;gap:0;font-size:16px;color:var(--white);font-weight:400}
.nav span{display:flex;align-items:center}
.nav span+span::before{content:"";width:4px;height:4px;border-radius:50%;background:var(--white);opacity:.7;margin:0 17px}
.nav .current{opacity:.75}
.social-dot{width:40px;height:40px;border-radius:50%}
.headline{left:0;width:1200px;top:125px;text-align:center;font-size:46px;line-height:58px;font-weight:400;color:var(--mauve);letter-spacing:1px}
.headline .light{color:var(--white)}
.form-label{font-size:15px;color:var(--white);letter-spacing:1px;top:409px}
.field{top:402px;height:36px;width:220px;background:var(--white);border:none;font:14px "Nunito Sans",sans-serif;color:#888;padding:0 14px;line-height:36px}
.btn{border:2px solid var(--pink);color:var(--pink);font-size:13px;letter-spacing:2px;text-align:center;border-radius:3px;text-transform:uppercase;font-weight:400;line-height:33px;height:37px}
.btn.ghost{border-color:var(--white);color:var(--white)}
.privacy{top:448px;left:0;width:1200px;text-align:center;font-size:10px;color:var(--white)}

/* Sections */
.section-title{left:0;width:1200px;text-align:center;font-size:28px;font-weight:300;color:var(--heading);letter-spacing:1px;text-transform:uppercase}
.product-cover{width:237px;height:232px;border:1px solid #ddd;box-shadow:0 3px 8px rgba(0,0,0,.15);background:#fff;padding:14px 40px}
.product-cover div{width:100%;height:100%}
.product-text{width:236px;font-size:15px;line-height:18.5px;color:var(--body-text)}
.testimonial{left:281px;width:612px;top:1183px;font-size:14px;line-height:19px;color:var(--body-text)}
.signature{left:797px;top:1260px;font-size:14px;color:var(--pink)}
.bio{left:348px;width:740px;font-size:14.5px;line-height:19px;color:var(--body-text)}
.portrait{left:123px;top:1385px;width:214px;height:214px;border-radius:50%;background:radial-gradient(circle at 50% 45%,#9a9a9a,#2b2b2b)}

/* Partner names */
.partner{font-size:30px;font-weight:600;color:var(--logo-grey);text-align:center;width:240px;transform:translateX(-50%)}
.partner.small{font-size:24px}
.partner-mark{display:inline-block;width:22px;height:22px;border-radius:50%;background:var(--logo-grey);vertical-align:middle;margin-right:8px}

/* Footer */
.footer{left:0;top:2005px;width:1200px;height:241px;background:var(--footer-bg)}
.footer .nav{font-size:15px}
.footer-col{font-size:13px;line-height:16px;color:var(--footer-text)}
.footer-col h4{font-size:15px;font-weight:400;margin-bottom:14px}
.footer-col p{opacity:.85}
</style>
</head>
<body>

<header class="hero" aria-label="Hero with soft floral backdrop" role="img"></header>
<div class="abs brand" style="left:40px;top:52px">DK Farrow</div>
<nav class="abs nav" style="left:242px;top:62px">
  <span class="current">Home</span><span>Products</span><span>About</span><span>Blog</span><span>Forum</span><span>Media Room</span><span>Success Stories</span>
</nav>
<div class="abs social-dot" style="left:1070px;top:53px;background:#3b5c9b" aria-label="Friendbook"></div>
<div class="abs social-dot" style="left:1119px;top:53px;background:#3fb1e6" aria-label="Chirper"></div>

<h1 class="abs headline">
  DISCOVER <span class="light">SECRETS</span><br>
  <span class="light">TO A</span><br>
  SLIMMER, SEXIER <span class="light">&amp;</span> HEALTHIER<br>
  <span class="light">YOU!</span>
</h1>

<div class="abs form-label" style="left:145px">NAME</div>
<div class="abs field" style="left:217px">Name</div>
<div class="abs form-label" style="left:503px">EMAIL</div>
<div class="abs field" style="left:579px">Email address</div>
<div class="abs btn ghost" style="left:855px;top:402px;width:198px">Subscribe</div>
<p class="abs privacy">* Email Privacy: Subscribe with complete confidence! We will never sell, rent, lease, or share your information with anyone.</p>

<!-- Products -->
<h2 class="abs section-title" style="top:522px">Products</h2>
<div class="abs btn" style="left:858px;top:522px;width:198px">View all products</div>

<div class="abs product-cover" style="left:124px;top:605px"><div role="img" aria-label="Green Juice Reset book cover" style="background:linear-gradient(180deg,#f1f6ea 0%,#9ccf6a 60%,#4f8a35 100%)"></div></div>
<div class="abs product-cover" style="left:481px;top:605px"><div role="img" aria-label="Slim Without Dieting book cover" style="background:linear-gradient(180deg,#f7c4dc 0%,#e34e99 100%)"></div></div>
<div class="abs product-cover" style="left:837px;top:605px"><div role="img" aria-label="Belly Fat Guide book cover" style="background:linear-gradient(180deg,#f5f5f5 0%,#f06a7e 60%,#d9264d 100%)"></div></div>

<p class="abs product-text" style="left:124px;top:861px">Lorem ipsum dolor sit amet, consectetur adipisicing elit, sed do eiusmod tempor incididunt ut labore et dolore magna aliqua. Ut enim ad minim veniam, quis nostrud exercitation ullamco laboris nisi ut aliquip ex ea consequat.</p>
<p class="abs product-text" style="left:483px;top:851px">Lorem ipsum dolor sit amet, consectetur adipisicing elit, sed do eiusmod tempor incididunt ut labore et dolore magna aliqua. Ut enim ad minim veniam, quis nostrud exercitation ullamco laboris nisi ut aliquip ex ea consequat.</p>
<p class="abs product-text" style="left:840px;top:850px">Lorem ipsum dolor sit amet, consectetur adipisicing elit, sed do eiusmod tempor incididunt ut labore et dolore magna aliqua. Ut enim ad minim veniam, quis nostrud exercitation ullamco laboris nisi ut aliquip ex ea consequat.</p>

<div class="abs btn" style="left:144px;top:1030px;width:197px">Read more</div>
<div class="abs btn" style="left:501px;top:1020px;width:197px">Read more</div>
<div class="abs btn" style="left:858px;top:1019px;width:198px">Read more</div>

<!-- Testimonials -->
<h2 class="abs section-title" style="top:1105px">Testimonials</h2>
<svg class="abs" style="left:204px;top:1208px" width="34" height="34" viewBox="0 0 34 34" aria-label="Previous">
  <circle cx="17" cy="17" r="15" fill="none" stroke="#d98cc1" stroke-width="2"/>
  <path d="M20 10 L13 17 L20 24 M13 17 H25" fill="none" stroke="#d98cc1" stroke-width="2"/>
</svg>
<svg class="abs" style="left:938px;top:1208px" width="34" height="34" viewBox="0 0 34 34" aria-label="Next">
  <circle cx="17" cy="17" r="15" fill="none" stroke="#d98cc1" stroke-width="2"/>
  <path d="M14 10 L21 17 L14 24 M21 17 H9" fill="none" stroke="#d98cc1" stroke-width="2"/>
</svg>
<p class="abs testimonial">Lorem ipsum dolor sit amet, consectetur adipisicing elit, sed do eiusmod tempor incididunt ut labore et dolore magna aliqua. Ut enim ad minim veniam, quis nostrud exercitation ullamco laboris nisi ut aliquip ex ea commodo consequat. Duis aute irure dolor in reprehenderit in voluptate velit esse cillum dolore eu fugiat nulla pariatur.</p>
<div class="abs signature">~ Happy Client</div>

<!-- About -->
<h2 class="abs section-title" style="top:1311px">Who is DK Farrow?</h2>
<div class="abs portrait" role="img" aria-label="Portrait photo of DK Farrow"></div>
<p class="abs bio" style="top:1403px">Lorem ipsum dolor sit amet, consectetur adipisicing elit, sed do eiusmod tempor incididunt ut labore et dolore magna aliqua. Ut enim ad minim veniam, quis nostrud exercitation ullamco laboris nisi ut aliquip ex ea commodo consequat. Duis aute irure dolor in reprehenderit in voluptate velit esse cillum dolore eu fugiat nulla pariatur. Excepteur sint occaecat cupidatat non proident, sunt in culpa qui officia deserunt mollit anim id est laborum.</p>
<p class="abs bio" style="top:1520px">At vero eos et accusamus et iusto odio dignissimos ducimus qui blanditiis praesentium voluptatum deleniti atque corrupti quos dolores et quas molestias excepturi sint occaecati cupiditate non provident, similique sunt in culpa qui officia deserunt mollitia animi, id est laborum et dolorum fuga.</p>
<div class="abs btn" style="left:870px;top:1614px;width:197px">Read more</div>

<!-- As seen on -->
<h2 class="abs section-title" style="top:1721px">As seen on</h2>
<div class="abs partner small" style="left:146px;top:1834px">Hearth Weekly</div>
<div class="abs partner small" style="left:444px;top:1834px">Lumina.example</div>
<div class="abs partner" style="left:741px;top:1830px">Channel Nine</div>
<div class="abs partner" style="left:1043px;top:1830px">Poise</div>
<div class="abs partner small" style="left:135px;top:1929px"><span class="partner-mark"></span>Beat Radio</div>
<div class="abs partner small" style="left:303px;top:1929px">Metro TV</div>
<div class="abs partner small" style="left:537px;top:1929px">OrbitWave Radio</div>
<div class="abs partner small" style="left:782px;top:1929px">Vista Net</div>
<div class="abs partner small" style="left:1016px;top:1929px">Civic Broadcast</div>

<!-- Footer -->
<footer class="abs footer"></footer>
<div class="abs brand" style="left:124px;top:2042px;font-size:28px">DK Farrow</div>
<nav class="abs nav footer-nav" style="left:367px;top:2050px;font-size:15px">
  <span>Home</span><span>Products</span><span>About</span><span>Blog</span><span>Forum</span><span>Media Room</span><span>Success Stories</span>
</nav>
<div class="abs footer-col" style="left:367px;top:2104px">
  <h4>Verana Publishing</h4>
  <p>4470 Linden Crest Rd<br>Suite 210<br>Harrowgate, MD 20999<br>202-555-0147</p>
</div>
<div class="abs footer-col" style="left:582px;top:2104px">
  <h4>Email</h4>
  <p>info@dkfarrowplace.example</p>
</div>
<div class="abs footer-col" style="left:777px;top:2104px">
  <h4>Social</h4>
  <p>Friendbook &nbsp;·&nbsp; Chirper</p>
</div>
<div class="abs footer-col" style="left:951px;top:2104px">
  <h4>© 2014</h4>
  <p>Verana Publishing</p>
</div>

</body>
</html>
```